Brackwell Downs Lamb Sticker Design

We need to create a design for sticky labels that will be placed meat packaging of individual cuts of meat for Brackwell Downs Lamb.

These sticke...

Target Market(s)

People who purchase Gourmet Meat Products. Higher income, Age 35-65

Industry/Entity Type

Farming

Requirements
Must have
• The Brackwell Downs Lamb Logo (attached)
• Quality Grass Fed Lamb
• Need to create a look of premium quality product.
• Space to write Net Weight
• Space to write $

```html
<!DOCTYPE html>
<html lang="en">
<head>
<meta charset="utf-8">
<title>Brackwell Downs Lamb – Cut Labels</title>
<link rel="stylesheet" href="https://fonts.googleapis.com/css2?family=Crimson+Pro:wght@700&family=Questrial&family=Oswald:wght@500&display=swap">
<style>
  :root {
    --ink: #111111;
    --paper: #ffffff;
  }
  html, body {
    margin: 0;
    padding: 0;
    overflow: hidden;
    background: var(--paper);
  }
  .sheet {
    position: relative;
    width: 1200px;
    height: 453px;
    background: var(--paper);
    overflow: hidden;
    color: var(--ink);
  }
  .label {
    position: absolute;
    top: 63px;
    width: 142px;
    height: 340px;
  }
  .label-shape {
    position: absolute;
    inset: 0;
    width: 142px;
    height: 340px;
  }
  .brand-name {
    position: absolute;
    left: 21px;
    top: 30px;
    width: 100px;
    height: 88px;
    display: flex;
    align-items: center;
    justify-content: center;
    text-align: center;
    font-family: "Crimson Pro", Georgia, serif;
    font-weight: 700;
    font-size: 16px;
    line-height: 1.1;
    color: var(--ink);
  }
  .label-body {
    position: absolute;
    left: 9px;
    right: 9px;
    top: 146px;
    display: flex;
    flex-direction: column;
    align-items: stretch;
    text-align: center;
  }
  .cut-name {
    height: 44px;
    display: flex;
    align-items: flex-end;
    justify-content: center;
    padding-bottom: 2px;
    border-bottom: 2px solid var(--ink);
    font-family: "Crimson Pro", Georgia, serif;
    font-weight: 700;
    font-size: 24px;
    line-height: 1;
  }
  .cut-name.two-line {
    font-size: 18px;
    line-height: 1.02;
  }
  .quality-block {
    height: 48px;
    border-bottom: 2px solid var(--ink);
    display: flex;
    flex-direction: column;
    justify-content: center;
  }
  .quality {
    font-family: "Questrial", Arial, sans-serif;
    font-size: 24px;
    line-height: 1;
  }
  .grass-fed {
    font-family: "Questrial", Arial, sans-serif;
    font-size: 10px;
    line-height: 1.2;
    margin-top: 2px;
  }
  .net-weight {
    font-family: "Questrial", Arial, sans-serif;
    font-size: 11px;
    margin-top: 3px;
  }
  .price {
    font-family: "Oswald", "Arial Narrow", sans-serif;
    font-weight: 500;
    font-size: 40px;
    line-height: 1;
    margin-top: 2px;
  }
</style>
</head>
<body>
<main class="sheet">

  <article class="label" style="left:38px">
    <svg class="label-shape" viewBox="0 0 142 340" aria-hidden="true">
      <path d="M2,100 V337 L71,313 L140,337 V100 Z" fill="var(--paper)" stroke="var(--ink)" stroke-width="2.5"/>
      <circle cx="71" cy="74" r="72" fill="var(--paper)" stroke="var(--ink)" stroke-width="2.5"/>
    </svg>
    <div class="brand-name">Brackwell Downs Lamb</div>
    <div class="label-body">
      <h2 class="cut-name" style="margin:0">Leg Roast</h2>
      <div class="quality-block">
        <div class="quality">Quality</div>
        <div class="grass-fed">Grass Fed Lamb</div>
      </div>
      <div class="net-weight">Net Weight : 50 gram</div>
      <div class="price">$250</div>
    </div>
  </article>

  <article class="label" style="left:283px">
    <svg class="label-shape" viewBox="0 0 142 340" aria-hidden="true">
      <path d="M2,100 V337 L71,313 L140,337 V100 Z" fill="var(--paper)" stroke="var(--ink)" stroke-width="2.5"/>
      <circle cx="71" cy="74" r="72" fill="var(--paper)" stroke="var(--ink)" stroke-width="2.5"/>
    </svg>
    <div class="brand-name">Brackwell Downs Lamb</div>
    <div class="label-body">
      <h2 class="cut-name" style="margin:0">Shoulder</h2>
      <div class="quality-block">
        <div class="quality">Quality</div>
        <div class="grass-fed">Grass Fed Lamb</div>
      </div>
      <div class="net-weight">Net Weight : 50 gram</div>
      <div class="price">$250</div>
    </div>
  </article>

  <article class="label" style="left:527px">
    <svg class="label-shape" viewBox="0 0 142 340" aria-hidden="true">
      <path d="M2,100 V337 L71,313 L140,337 V100 Z" fill="var(--paper)" stroke="var(--ink)" stroke-width="2.5"/>
      <circle cx="71" cy="74" r="72" fill="var(--paper)" stroke="var(--ink)" stroke-width="2.5"/>
    </svg>
    <div class="brand-name">Brackwell Downs Lamb</div>
    <div class="label-body">
      <h2 class="cut-name two-line" style="margin:0">Fore<br>Quarter Chops</h2>
      <div class="quality-block">
        <div class="quality">Quality</div>
        <div class="grass-fed">Grass Fed Lamb</div>
      </div>
      <div class="net-weight">Net Weight : 50 gram</div>
      <div class="price">$250</div>
    </div>
  </article>

  <article class="label" style="left:772px">
    <svg class="label-shape" viewBox="0 0 142 340" aria-hidden="true">
      <path d="M2,100 V337 L71,313 L140,337 V100 Z" fill="var(--paper)" stroke="var(--ink)" stroke-width="2.5"/>
      <circle cx="71" cy="74" r="72" fill="var(--paper)" stroke="var(--ink)" stroke-width="2.5"/>
    </svg>
    <div class="brand-name">Brackwell Downs Lamb</div>
    <div class="label-body">
      <h2 class="cut-name" style="margin:0">Lamb Neck</h2>
      <div class="quality-block">
        <div class="quality">Quality</div>
        <div class="grass-fed">Grass Fed Lamb</div>
      </div>
      <div class="net-weight">Net Weight : 50 gram</div>
      <div class="price">$250</div>
    </div>
  </article>

  <article class="label" style="left:1016px">
    <svg class="label-shape" viewBox="0 0 142 340" aria-hidden="true">
      <path d="M2,100 V337 L71,313 L140,337 V100 Z" fill="var(--paper)" stroke="var(--ink)" stroke-width="2.5"/>
      <circle cx="71" cy="74" r="72" fill="var(--paper)" stroke="var(--ink)" stroke-width="2.5"/>
    </svg>
    <div class="brand-name">Brackwell Downs Lamb</div>
    <div class="label-body">
      <h2 class="cut-name" style="margin:0;font-size:20px">Lamb Shanks</h2>
      <div class="quality-block">
        <div class="quality">Quality</div>
        <div class="grass-fed">Grass Fed Lamb</div>
      </div>
      <div class="net-weight">Net Weight : 50 gram</div>
      <div class="price">$250</div>
    </div>
  </article>

</main>
</body>
</html>
```